Information security company needs poster for trade show

We do a lot of trade shows and need a sign/poster with our name to hang up so people know whose booth they are seeing. This would be something that goes on a table-top easel. This particular poster will be used at health-care trade shows.

Attached is our existing sign and our new logo. we'd like to use the logo and some color scheme that works with that.

The wording on the existing sign should be on the design if possible

Industry/Entity Type

Security

```html
<!DOCTYPE html>
<html lang="en">
<head>
<meta charset="utf-8">
<title>Corvale Group — Trade Show Poster</title>
<link rel="stylesheet" href="https://fonts.googleapis.com/css2?family=Sorts+Mill+Goudy:ital@0;1&display=swap">
<style>
  :root {
    --ink-white: #f4f7fa;
    --accent-cyan: #7fd6ee;
    --brand-blue: #2336b0;
    --brand-ring: #cfd6de;
    --rack-blue: #2f8db4;
    --rack-deep: #10405c;
    --suit-dark: #0d1217;
    --glow-teal: rgba(120, 225, 240, 0.45);
    --skin-warm: rgba(214, 170, 140, 0.55);
    --shirt-grey: rgba(150, 175, 195, 0.55);
  }
  html, body {
    margin: 0;
    padding: 0;
    overflow: hidden;
    background: #000;
  }
  .poster {
    position: relative;
    width: 1200px;
    height: 927px;
    overflow: hidden;
  }
  .backdrop {
    position: absolute;
    inset: 0;
    background:
      radial-gradient(ellipse 260px 90px at 800px 720px, rgba(235, 245, 250, 0.55), rgba(235, 245, 250, 0) 75%),
      radial-gradient(ellipse 170px 200px at 1090px 600px, var(--skin-warm), rgba(214, 170, 140, 0) 72%),
      radial-gradient(ellipse 120px 110px at 560px 690px, rgba(214, 170, 140, 0.4), rgba(214, 170, 140, 0) 72%),
      radial-gradient(ellipse 120px 260px at 1010px 130px, var(--shirt-grey), rgba(150, 175, 195, 0) 75%),
      radial-gradient(circle 190px at 770px 450px, var(--glow-teal), rgba(120, 225, 240, 0.12) 60%, rgba(120, 225, 240, 0) 100%),
      radial-gradient(ellipse 300px 640px at 1000px 430px, rgba(13, 18, 23, 0.95), rgba(13, 18, 23, 0) 80%),
      linear-gradient(90deg,
        #1b5f80 0%, var(--rack-blue) 9%, #1d6d92 16%, #3a9cc4 24%,
        #1b6688 32%, var(--rack-deep) 44%, #16242f 58%, var(--suit-dark) 72%, #121a20 100%);
  }
  .brand {
    position: absolute;
    left: 75px;
    top: 112px;
    display: flex;
    align-items: center;
    gap: 14px;
  }
  .brand-dot {
    width: 186px;
    height: 186px;
    border-radius: 50%;
    background: var(--brand-blue);
  }
  .brand-name {
    font-family: "Sorts Mill Goudy", serif;
    font-size: 44px;
    line-height: 40px;
    letter-spacing: 2px;
    color: var(--ink-white);
  }
  .tagline {
    position: absolute;
    left: 82px;
    top: 368px;
    margin: 0;
    font-weight: 400;
  }
  .tagline-lead {
    display: block;
    font-family: "Sorts Mill Goudy", serif;
    font-style: italic;
    font-size: 38px;
    line-height: 44px;
    color: var(--accent-cyan);
    margin-bottom: 18px;
  }
  .tagline-main {
    display: block;
    font-family: "Sorts Mill Goudy", serif;
    font-size: 57px;
    line-height: 67px;
    color: var(--ink-white);
    text-shadow: 0 2px 6px rgba(0, 0, 0, 0.5);
  }
  .web-address {
    position: absolute;
    left: 750px;
    top: 848px;
    font-family: "Sorts Mill Goudy", serif;
    font-size: 27px;
    color: var(--ink-white);
  }
</style>
</head>
<body>
  <main class="poster">
    <div class="backdrop" role="img" aria-label="Photo of a businessman in a dark suit and blue tie touching a tablet, with glowing security icons around a padlock floating above it, in front of blue-lit server racks"></div>

    <div class="brand">
      <span class="brand-dot"></span>
      <span class="brand-name">CORVALE<br>GROUP</span>
    </div>

    <h1 class="tagline">
      <span class="tagline-lead">Specializing in</span>
      <span class="tagline-main">HIPAA Compliance<br>&amp;&nbsp; Information Security</span>
    </h1>

    <div class="web-address">www.corvalegroup.com</div>
  </main>
</body>
</html>
```